Zielgruppe
Steuerberatung
Aufgabenstellung
Ich benötige eine Neuerstellung für ein vorhandenes Briefpapier. Bedeutet, eigentlich soll der aktuelle Inhalt neu erstellt werden, da mir die Rohdaten nicht mehr zur Verfügung stehen. Das aktuelle Briefpapier steht als .doc zur Verfügung. Ziel 1:1 Abbildung. Zudem muss die Adresse geändert werden.

```html
<!DOCTYPE html>
<html lang="de">
<head>
<meta charset="utf-8">
<title>Briefpapier – Jonas Brettner Steuerberater</title>
<link href="https://fonts.googleapis.com/css2?family=Archivo+Narrow:wght@400;700&display=swap" rel="stylesheet">
<style>
  :root {
    --backdrop: #808080;
    --paper: #ffffff;
    --ink: #111111;
    --mark: #4a4a4a;
    --band: #474745;
  }
  * { margin: 0; padding: 0; box-sizing: border-box; }
  html, body { width: 1200px; height: 1200px; overflow: hidden; }
  body {
    background: var(--backdrop);
    font-family: "Archivo Narrow", "Arial Narrow", sans-serif;
    color: var(--ink);
    position: relative;
  }
  .letterhead {
    position: absolute;
    left: 240px; top: 91px;
    width: 718px; height: 1017px;
    background: var(--paper);
    overflow: hidden;
  }
  .sender-line {
    position: absolute;
    left: 67px; top: 152px;
    font-size: 7.6px;
    white-space: nowrap;
  }
  .brand {
    position: absolute;
    left: 521px; top: 57px;
    display: flex; align-items: center; gap: 8px;
  }
  .brand-square {
    width: 14px; height: 14px;
    border: 1.2px solid var(--mark);
  }
  .brand-name {
    font-size: 14px;
    color: var(--mark);
    font-weight: 400;
  }
  .contact {
    position: absolute;
    left: 521px; top: 150px;
    font-size: 10px;
    line-height: 14.4px;
  }
  .contact strong { font-weight: 700; }
  .contact-row { display: flex; }
  .contact-label { width: 24px; }
  .footer {
    position: absolute;
    left: 67px; top: 1031px;
    top: 940px;
    font-size: 9.6px;
    line-height: 14.4px;
    white-space: nowrap;
  }
  .footer strong { font-weight: 700; }
  .band {
    position: absolute;
    left: 0; bottom: 0;
    width: 100%; height: 23px;
    background: var(--band);
  }
</style>
</head>
<body>
  <main class="letterhead">
    <p class="sender-line">Jonas Brettner &nbsp;|&nbsp; Lindenhofstr. 118 &nbsp;|&nbsp; 30159 Hannover</p>

    <div class="brand">
      <span class="brand-square"></span>
      <span class="brand-name">Brettner</span>
    </div>

    <address class="contact" style="font-style:normal">
      <div><strong>Jonas Brettner</strong> | Steuerberater</div>
      <div class="contact-row"><span class="contact-label">Tel.:</span><span>+49 (0) 170 - 55 20 631</span></div>
      <div class="contact-row"><span class="contact-label">Fax.:</span><span>+49 (0) 511 - 86 21 90 44</span></div>
      <div class="contact-row"><span class="contact-label">Mail:</span><span>info@steuerberatung-brettner.de</span></div>
      <div class="contact-row"><span class="contact-label">Web:</span><span>www.steuerberatung-brettner.de</span></div>
    </address>

    <footer class="footer">
      <div><strong>Jonas Brettner</strong> | Steuerberater</div>
      <div>Lindenhofstr. 118 &nbsp;|&nbsp; 30159 Hannover &nbsp;|&nbsp; Zuständige Aufsichtsbehörde: Steuerberaterkammer Nordland -Körperschaft des öffentlichen Rechts-</div>
      <div>Zuständiges Finanzamt: Finanzamt Lindenhof-Mitte, Steuernummer: 31/208/47716 &nbsp;|&nbsp; Bankverbindung: DE 00 1234 5678 9012 3456 78 BIC: BANKDEXX</div>
    </footer>

    <div class="band"></div>
  </main>
</body>
</html>
```